Redesign our updated cannabis seeds website

We are updating our website. Our current website is www.moorkernels.nl or new website is www.kroonvelden.info.

We need an updated design for:
-home page (www.kroonvelden.info) everything between the menu and the footer can be changed. The text we want to keep the same. Suggestions for adding content to the homepage top 5 THC strains, top 5 High Yield, Best Outdoor Cannabis Strains, Best Selling Strains.
-product pages Female Seeds (https://kroonvelden.info/product-category/female-seeds/), Regular Seeds (https://kroonvelden.info/product-category/regular-seeds/) , Autoflower Seeds(https://kroonvelden.info/product-category/autoflowering-seeds/). Everything between the header and the footer can be changed.
-the shop page https://kroonvelden.info/shop/ everything between the main menu and the footer.
-FAQ page https://kroonvelden.info/faqs/ everything between the main menu and the footer.
-Contact page https://kroonvelden.info/contact/ everything between the main menu and the footer.
-Terms and conditions, Shipment Policy, Return Policy, Disclaimer, Cookie Policy, Intellectual Property Claims pages everything between the main menu and the footer.
-All options under my account.

You can login as a customer as:
webteam@moorkern.nl
Kq7&Tz2m!Rw9#Lp4Xc8@Vb3N

Colors to us:
dark green=004820
light green=C7DC67
black= 222 
white= FFFFFF
orange=ff7a04
font color= #222

Preferred fonts:
Header font: Francois One
Body font: Lato

We prefer the artwork files as vector files if possible.

Attached samples of how our packaging looks.
Also under this link www.moorkernels.nl/promokit you can find more images. If any other images are missing that you need please let us know.

Europe

cannabis seeds

5+ page

00AB8E
00BBA5
67D7C9
C6EFE9
E9F9F6
59FF00
82FF00
B8FF75
E3FFCB
F4FFEA

• House colors.

```html
<!DOCTYPE html>
<html lang="en">
<head>
<meta charset="utf-8">
<title>Contact Us – Moor Kernels</title>
<link href="https://fonts.googleapis.com/css2?family=Francois+One&family=Lato:wght@400;700&display=swap" rel="stylesheet">
<style>
:root{
  --green:#004820;
  --light:#c7dc67;
  --accent:#a6bf3f;
  --ink:#222222;
  --white:#ffffff;
  --orange:#ff7a04;
  --line:#cfcfcf;
}
*{box-sizing:border-box;margin:0;padding:0}
html,body{width:1200px;height:2229px;overflow:hidden}
body{position:relative;font-family:'Lato',sans-serif;color:var(--ink);background:var(--white)}
.abs{position:absolute}
.head{font-family:'Francois One',sans-serif;text-transform:uppercase}
svg{display:block}

/* header */
.brand{left:112px;top:22px;width:175px;height:80px;display:flex;align-items:center;gap:8px}
.brand-mark{width:20px;height:20px;border-radius:50%;background:var(--accent);flex:none}
.brand-name{font-weight:700;font-size:21px;color:var(--green);white-space:nowrap}
.topbar{left:431px;top:11px;display:flex;align-items:center;font-size:17px;color:var(--ink);gap:0;white-space:nowrap}
.shop-tag{background:var(--green);color:var(--white);font-weight:700;font-size:16px;padding:0 10px;height:31px;line-height:31px;margin-right:15px}
.topbar .item{display:flex;align-items:center;gap:5px}
.topbar .sep{margin:0 11px}
.topbar .active{color:var(--accent)}
.nav{left:325px;top:69px;display:flex;gap:17px;font-size:17px;white-space:nowrap}
.tool{width:45px;height:45px;border-radius:50%;border:1px solid var(--ink);display:flex;align-items:center;justify-content:center;top:58px}
.tool.cart{background:var(--green);border-color:var(--green)}

/* hero */
.hero{left:0;top:118px;width:1200px;height:313px;background:linear-gradient(100deg,#b76a5a 0%,#7f8f48 18%,#5f8a3a 45%,#6e9545 65%,#8fa85d 85%,#a9b06c 100%)}
.hero h1{position:absolute;left:0;right:0;top:110px;text-align:center;font-family:'Francois One',sans-serif;font-size:76px;font-weight:400;color:var(--white);letter-spacing:1px;line-height:1}

/* breadcrumb */
.crumb{left:111px;top:460px;font-size:19px;white-space:nowrap}
.crumb .here{color:var(--accent)}
.crumb .gt{margin:0 8px 0 12px}
.rule{left:111px;top:502px;width:977px;height:1px;background:var(--line)}

/* form */
.msg-title{left:111px;top:568px;font-size:44px;color:var(--green);line-height:1}
.msg-text{left:113px;top:647px;width:570px;font-size:16px;line-height:30px}
.field{left:112px;width:558px;height:57px;border:1px solid #bdbdbd;font-size:17px;padding:17px 16px;color:#444}
.field.area{height:126px}
.send{left:112px;top:1126px;width:121px;height:60px;border-radius:30px;background:var(--orange);color:var(--white);font-weight:700;font-size:20px;display:flex;align-items:center;justify-content:center}

/* contact info */
.info{left:736px;top:577px;width:352px;height:555px;background:var(--green);color:var(--white)}
.info h2{position:absolute;left:37px;top:38px;font-family:'Francois One',sans-serif;font-weight:400;font-size:27px}
.info-row{position:absolute;left:37px;display:flex;gap:21px;font-size:16px;line-height:22.5px}
.ring{width:44px;height:44px;border-radius:50%;border:1.5px solid var(--white);display:flex;align-items:center;justify-content:center;flex:none}

/* updates */
.updates{left:0;top:1272px;width:1200px;height:364px;background:radial-gradient(ellipse at 50% 45%,#b7d35d 0%,#c3db6b 45%,#bcd562 75%,#b1cd57 100%)}
.updates h2{position:absolute;left:0;right:0;top:90px;text-align:center;font-family:'Francois One',sans-serif;font-weight:400;font-size:46px;color:var(--white)}
.updates p{position:absolute;left:0;right:0;top:158px;text-align:center;font-size:17px;color:var(--white)}
.sub-field{top:216px;height:58px;background:var(--white);font-size:19px;padding:18px 17px;color:#444}
.sub-btn{left:922px;top:215px;width:155px;height:60px;border-radius:30px;background:var(--orange);color:var(--white);font-weight:700;font-size:20px;display:flex;align-items:center;justify-content:center}

/* footer */
.footer{left:0;top:1636px;width:1200px;height:593px;background:var(--green);color:var(--white)}
.f-brand{left:106px;top:35px;width:272px;height:184px;background:#0b3f1c;display:flex;align-items:center;justify-content:center;gap:10px}
.f-brand .brand-mark{background:var(--light)}
.f-brand span{font-weight:700;font-size:26px;color:var(--light)}
.f-contact{left:111px;display:flex;gap:13px;font-size:17px;line-height:22px}
.cards{left:108px;top:418px;display:flex;gap:30px}
.card{width:78px;height:46px;border-radius:6px;background:#0b3f1c;border:1px solid #2c6a3f;display:flex;align-items:center;justify-content:center;font-weight:700;font-size:15px;color:var(--white)}
.col{top:78px}
.col h3{font-family:'Francois One',sans-serif;font-weight:400;font-size:22px;letter-spacing:.4px;margin-bottom:26px;text-transform:uppercase}
.col ul{list-style:none;font-size:16.5px;line-height:22.5px}
.cats li{margin-bottom:20px}
.f-rule{left:111px;top:489px;width:977px;height:1px;background:#3c7050}
.copy{left:111px;top:527px;font-size:17px}
.social{top:518px;width:43px;height:43px;border-radius:50%;border:1px solid var(--white)}
</style>
</head>
<body>

<!-- header -->
<div class="abs brand"><span class="brand-mark"></span><span class="brand-name">Moor Kernels</span></div>

<div class="abs topbar">
  <span class="shop-tag">SHOP</span>
  <span class="item"><svg width="15" height="15" viewBox="0 0 16 16"><circle cx="8" cy="8" r="8" fill="#c7dc67"/><text x="8" y="12" font-size="11" font-family="Lato" font-weight="700" text-anchor="middle" fill="#fff">?</text></svg>FAQs</span>
  <span class="sep">|</span>
  <span class="item active"><svg width="15" height="15" viewBox="0 0 16 16"><circle cx="8" cy="8" r="8" fill="#c7dc67"/><text x="8" y="12" font-size="11" font-family="Lato" font-weight="700" text-anchor="middle" fill="#fff">?</text></svg>Contact Us</span>
  <span class="sep">|</span>
  <span class="item"><svg width="18" height="13" viewBox="0 0 18 13"><rect width="18" height="13" rx="1" fill="#c7dc67"/><path d="M0 1l9 6 9-6" stroke="#fff" stroke-width="1.5" fill="none"/></svg>info@moorkernels.nl</span>
  <span class="sep">|</span>
  <span class="item"><svg width="15" height="15" viewBox="0 0 24 24"><path d="M6.6 10.8a15 15 0 006.6 6.6l2.2-2.2a1 1 0 011-.25 11.4 11.4 0 003.6.57 1 1 0 011 1V20a1 1 0 01-1 1A17 17 0 013 4a1 1 0 011-1h3.5a1 1 0 011 1c0 1.25.2 2.45.57 3.57a1 1 0 01-.25 1z" fill="#c7dc67"/></svg>+31 (0)20 – 555 0142</span>
</div>

<nav class="abs nav">
  <span>Cannabis Movies</span><span>Female Seeds</span><span>Regular Seeds</span><span>Autoflowering Seeds</span><span>Blog</span>
</nav>

<div class="abs tool" style="left:942px"><svg width="18" height="18" viewBox="0 0 20 20"><circle cx="8" cy="8" r="6" stroke="#222" stroke-width="2.6" fill="none"/><path d="M12.5 12.5l5 5" stroke="#222" stroke-width="2.8" stroke-linecap="round"/></svg></div>
<div class="abs tool" style="left:994px"><svg width="16" height="17" viewBox="0 0 16 17"><circle cx="8" cy="5" r="4" fill="#222"/><path d="M1 17c0-5 3-7.5 7-7.5s7 2.5 7 7.5z" fill="#222"/></svg></div>
<div class="abs tool cart" style="left:1044px"><svg width="20" height="18" viewBox="0 0 20 18"><path d="M1 1h3l2.2 10h10.5L19 4H5" stroke="#fff" stroke-width="2" fill="none" stroke-linejoin="round"/><path d="M5.5 4h13.3l-2.1 7H6.2z" fill="#fff"/><circle cx="7.5" cy="15.5" r="1.8" fill="#fff"/><circle cx="15.5" cy="15.5" r="1.8" fill="#fff"/></svg></div>

<!-- hero -->
<section class="abs hero" role="img" aria-label="Close-up photograph of a flowering cannabis bud">
  <h1>CONTACT US</h1>
</section>

<div class="abs crumb"><span>Home</span><span class="gt">&gt;&gt;</span><span class="here">Contact Us</span></div>
<div class="abs rule"></div>

<!-- message form -->
<h2 class="abs head msg-title">Message Us</h2>
<p class="abs msg-text">Thank you for using Moor Kernels! Please complete this form, So we can provide Quick and Efficient Service! If you have urgent</p>

<div class="abs field" style="top:746px">Your Name *</div>
<div class="abs field" style="top:816px">Your Email *</div>
<div class="abs field" style="top:886px">Subject</div>
<div class="abs field area" style="top:956px">Message</div>
<div class="abs send">SEND</div>

<!-- contact info -->
<aside class="abs info">
  <h2>Contact Information</h2>
  <div class="info-row" style="top:101px">
    <span class="ring" style="margin-top:2px"><svg width="14" height="20" viewBox="0 0 14 20"><path d="M7 0a7 7 0 00-7 7c0 5 7 13 7 13s7-8 7-13a7 7 0 00-7-7z" fill="#c7dc67"/><circle cx="7" cy="7" r="2.5" fill="#004820"/></svg></span>
    <span>MOOR KERNELS®<br>Veldkade 14<br>1052 KP Amsterdam<br>Nederland</span>
  </div>
  <div class="info-row" style="top:229px">
    <span class="ring" style="margin-top:2px"><svg width="18" height="18" viewBox="0 0 24 24"><path d="M6.6 10.8a15 15 0 006.6 6.6l2.2-2.2a1 1 0 011-.25 11.4 11.4 0 003.6.57 1 1 0 011 1V20a1 1 0 01-1 1A17 17 0 013 4a1 1 0 011-1h3.5a1 1 0 011 1c0 1.25.2 2.45.57 3.57a1 1 0 01-.25 1z" fill="#c7dc67"/></svg></span>
    <span>Phone:<br>+31 (0)20 – 555 0142</span>
  </div>
  <div class="info-row" style="top:320px">
    <span class="ring" style="margin-top:2px"><svg width="20" height="20" viewBox="0 0 20 20"><rect x="1" y="6" width="4" height="13" rx="1" fill="#c7dc67"/><rect x="6" y="6" width="13" height="13" rx="1" fill="#c7dc67"/><rect x="8" y="1" width="9" height="6" fill="none" stroke="#c7dc67" stroke-width="1.5"/><g fill="#004820"><rect x="8" y="9" width="9" height="2.5"/><rect x="8" y="13" width="2" height="2"/><rect x="11.5" y="13" width="2" height="2"/><rect x="15" y="13" width="2" height="2"/><rect x="8" y="16" width="2" height="2"/><rect x="11.5" y="16" width="2" height="2"/><rect x="15" y="16" width="2" height="2"/></g></svg></span>
    <span>Fax:<br>+31 (0)20 – 555 0143</span>
  </div>
  <div class="info-row" style="top:415px">
    <span class="ring" style="margin-top:2px"><svg width="22" height="16" viewBox="0 0 22 16"><rect width="22" height="16" rx="2" fill="#c7dc67"/><path d="M1 2l10 7 10-7" stroke="#004820" stroke-width="1.8" fill="none"/></svg></span>
    <span>E-mail:<br>info@moorkernels.nl</span>
  </div>
</aside>

<!-- updates -->
<section class="abs updates" role="img" aria-label="Soft-focus light green cannabis plant background">
  <h2>GET OUR UPDATES</h2>
  <p>Sign up and stay in the know! Subscribe to get the latest Moor Kernels news and exclusive offers.</p>
  <div class="abs sub-field" style="left:123px;width:384px">Name</div>
  <div class="abs sub-field" style="left:522px;width:385px">Email</div>
  <div class="abs sub-btn">SUBSCRIBE</div>
</section>

<!-- footer -->
<footer class="abs footer">
  <div class="abs f-brand"><span class="brand-mark"></span><span>Moor Kernels</span></div>

  <div class="abs f-contact" style="top:250px"><svg width="20" height="15" viewBox="0 0 22 16" style="margin-top:3px"><rect width="22" height="16" rx="2" fill="#c7dc67"/><path d="M1 2l10 7 10-7" stroke="#004820" stroke-width="1.8" fill="none"/></svg><span>info@moorkernels.nl</span></div>
  <div class="abs f-contact" style="top:296px"><svg width="17" height="17" viewBox="0 0 24 24" style="margin-top:2px"><path d="M6.6 10.8a15 15 0 006.6 6.6l2.2-2.2a1 1 0 011-.25 11.4 11.4 0 003.6.57 1 1 0 011 1V20a1 1 0 01-1 1A17 17 0 013 4a1 1 0 011-1h3.5a1 1 0 011 1c0 1.25.2 2.45.57 3.57a1 1 0 01-.25 1z" fill="#c7dc67"/></svg><span>+31 (0)20 – 555 0142</span></div>
  <div class="abs f-contact" style="top:343px"><svg width="12" height="18" viewBox="0 0 14 20" style="margin-top:2px"><path d="M7 0a7 7 0 00-7 7c0 5 7 13 7 13s7-8 7-13a7 7 0 00-7-7z" fill="#c7dc67"/><circle cx="7" cy="7" r="2.5" fill="#004820"/></svg><span>Veldkade 14 1052KP<br>Amsterdam Nederland</span></div>

  <div class="abs cards"><span class="card">Paycard</span><span class="card">Cardlink</span></div>

  <div class="abs col cats" style="left:443px;width:200px">
    <h3>Categories</h3>
    <ul>
      <li>Autoflowering Cannabis Seeds</li>
      <li>Buy Cannabis Seeds</li>
      <li>Cannabis Aroma Flavor And Medicinal Benefits</li>
      <li>Cannabis Seeds</li>
      <li>Cannabis Aroma Flavor And Medicinal Benefits</li>
    </ul>
  </div>
  <div class="abs col" style="left:695px">
    <h3>My Account</h3>
    <ul><li>Checkout</li><li>My Account</li><li>Shop</li><li>Orders</li><li>Account details</li><li>Lost password</li></ul>
  </div>
  <div class="abs col" style="left:888px">
    <h3>Quick Links</h3>
    <ul><li>Shop</li><li>FAQs</li><li>Contact us</li><li>Terms &amp; Conditions</li><li>Shipment Policy</li><li>Return Policy</li><li>Disclaimer</li><li>Cookie Policy</li><li>Intellectual Property Claims</li></ul>
  </div>

  <div class="abs f-rule"></div>
  <p class="abs copy">Copyright © 2024, Moor Kernels. All rights reserved.</p>
  <span class="abs social" style="left:842px" aria-label="Social link"></span>
  <span class="abs social" style="left:893px" aria-label="Social link"></span>
  <span class="abs social" style="left:944px" aria-label="Social link"></span>
  <span class="abs social" style="left:995px" aria-label="Social link"></span>
  <span class="abs social" style="left:1046px" aria-label="Social link"></span>
</footer>

</body>
</html>
```